Food label for BarBQ sauce and creole seasoning under the name GOLDEN MERCY

I need a label design using the name "GOLDEN MERCY" that will be used on bottles of Bar B Q sauce, both Creole and Cajun, and dry Cajun and dry Creole seasoning. I have attached a copy of the letter style we will be using. It is NOT a religious product or has any religious meaning. It comes from a saying old southerners used when they tasted something special -"Oh Golden Mercy". The labels for the Bar B Q sauces will be 5" wide by 3" tall, and the dry seasonings will be 5" wide by 3 1/2" tall. The products will that they are from South Louisiana and should reflect the typical food from the New Orleans area. This produce name is a REGISTERED TRADE NAME with the US trademark office.

```html
<!DOCTYPE html>
<html lang="en">
<head>
<meta charset="utf-8">
<title>Golden Mercy – Product Labels</title>
<link rel="stylesheet" href="https://fonts.googleapis.com/css2?family=Rye&family=Rokkitt:wght@800&display=swap">
<style>
  :root {
    --page-bg: #ffffff;
    --ink: #2b2b2b;
    --gold-light: #f8c51c;
    --gold-deep: #e39c00;
    --gold-text: #f5c227;
    --orange-light: #f6b46a;
    --orange-deep: #e8853a;
    --peach-text: #f4c48a;
  }
  * { margin: 0; padding: 0; box-sizing: border-box; }
  html, body {
    width: 1200px;
    height: 900px;
    overflow: hidden;
    background: var(--page-bg);
  }
  .canvas {
    position: relative;
    width: 1200px;
    height: 900px;
  }
  .label {
    position: absolute;
    width: 715px;
    height: 427px;
    overflow: hidden;
  }
  .label--seasoning { left: 51px; top: 22px; }
  .label--sauce { left: 408px; top: 451px; }

  .label__wood {
    position: absolute;
    inset: 0;
  }
  .label--seasoning .label__wood {
    background:
      repeating-linear-gradient(90deg, rgba(0,0,0,0) 0 58px, rgba(150,90,0,0.12) 58px 60px),
      radial-gradient(ellipse at 30% 30%, var(--gold-light), var(--gold-deep) 90%);
  }
  .label--sauce .label__wood {
    background:
      repeating-linear-gradient(90deg, rgba(0,0,0,0) 0 58px, rgba(150,70,20,0.12) 58px 60px),
      radial-gradient(ellipse at 40% 30%, var(--orange-light), var(--orange-deep) 95%);
  }

  .label__name {
    position: absolute;
    left: 0;
    right: 0;
    top: 14px;
    text-align: center;
    font-family: "Rye", serif;
    color: var(--ink);
    font-size: 112px;
    line-height: 128px;
    letter-spacing: -2px;
  }
  .label__name span { display: block; }

  .label__band {
    position: absolute;
    left: 0;
    top: 287px;
    width: 715px;
    height: 140px;
    fill: var(--ink);
  }

  .label__product {
    position: absolute;
    left: 0;
    right: 0;
    top: 330px;
    text-align: center;
    font-family: "Rokkitt", serif;
    font-weight: 800;
    font-size: 33px;
    line-height: 35px;
    letter-spacing: 0.5px;
  }
  .label--seasoning .label__product { color: var(--gold-text); }
  .label--sauce .label__product { color: var(--peach-text); }
</style>
</head>
<body>
<main class="canvas">

  <section class="label label--seasoning">
    <div class="label__wood" role="img" aria-label="Weathered golden yellow wood plank texture"></div>
    <h1 class="label__name"><span>GOLDEN</span><span>MERCY</span></h1>
    <svg class="label__band" viewBox="0 0 715 140" preserveAspectRatio="none" aria-hidden="true">
      <polygon points="0,36 18,30 34,38 52,28 80,34 110,26 140,31 170,22 200,30 230,24 262,33 290,20 320,28 350,24 380,34 410,26 440,30 470,22 500,32 530,26 560,38 590,28 620,34 650,24 680,33 700,26 715,30 715,140 0,140"/>
    </svg>
    <p class="label__product">DRY CAJUN<br>SEASONING</p>
  </section>

  <section class="label label--sauce">
    <div class="label__wood" role="img" aria-label="Weathered orange wood plank texture"></div>
    <h2 class="label__name"><span>GOLDEN</span><span>MERCY</span></h2>
    <svg class="label__band" viewBox="0 0 715 140" preserveAspectRatio="none" aria-hidden="true">
      <polygon points="0,34 20,28 40,36 62,26 90,32 118,24 146,30 176,22 204,31 234,25 264,34 292,21 322,29 352,23 382,33 412,27 442,31 472,22 502,33 532,25 562,36 592,27 622,33 652,23 682,32 702,25 715,29 715,140 0,140"/>
    </svg>
    <p class="label__product">BARBQ SAUCE<br>CAJUN</p>
  </section>

</main>
</body>
</html>
```